Menu Design Project

We trying to replace old flyer/menu with some new design.
hello this is my old menu i attached in email and my logo, the text you can pick from the menu and and i also attached some new picture for the food ,with my menu size unfold. front and back and then fold to 3.5" * 11". please show me what best can you do .Trifold is fine but must have image of food,
this is indian Restaurant
thats fine to have trifold menu design do to short time

Need to add also food picture on menu

Font styles to use
Serif
Decorative
Script

Colors

Designer to choose colors to be used in the design.

Requirements
Must have
• food image on menu
• trifold is fine ( do to short time)
• menu has to elegant ,color or text can be optional, Menu need to be neat and clean no too much rush on between the words .

```html
<!DOCTYPE html>
<html lang="en">
<head>
<meta charset="utf-8">
<title>Saffron Court – Outer Menu</title>
<link href="https://fonts.googleapis.com/css2?family=Oswald:wght@300;400;500;600&family=Open+Sans:ital,wght@0,400;0,600;1,400&family=Rye&family=Courgette&display=swap" rel="stylesheet">
<style>
:root{
  --chalk:#1c1c1c;
  --chalk-light:#2b2b2b;
  --paper:#ffffff;
  --ink:#161616;
  --muted:#555;
  --muted-dark:#b9b9b9;
  --gold-dark:#b2832b;
  --gold-light:#f4dc92;
}
*{box-sizing:border-box}
html,body{margin:0;padding:0}
body{width:1200px;height:1002px;overflow:hidden;background:var(--paper);font-family:"Open Sans",sans-serif;color:var(--ink)}
.menu{display:grid;grid-template-columns:repeat(3,400px);width:1200px;height:1002px}
.panel{position:relative;height:1002px;display:flex;flex-direction:column;border-right:1px solid #e2e2e2}
.chalk{background:radial-gradient(ellipse at 40% 30%,var(--chalk-light),var(--chalk) 70%);color:#fff}
.ribbon{display:inline-block;background:linear-gradient(90deg,var(--gold-dark),var(--gold-light) 50%,var(--gold-dark));color:#1a1a1a;font:500 14px "Oswald",sans-serif;letter-spacing:.3px;padding:3px 20px;clip-path:polygon(0 0,100% 0,95% 50%,100% 100%,0 100%,5% 50%);text-transform:uppercase;white-space:nowrap}
.ribbon::after{content:" ✦";font-size:9px}
.item{display:grid;grid-template-columns:1fr auto;column-gap:6px}
.item .name{font-size:10px;font-weight:600}
.item .price{font-size:10px}
.item .desc{grid-column:1/3;font-size:7.2px;font-style:italic;line-height:1.2;color:var(--muted)}
.chalk .item .desc{color:var(--muted-dark)}
/* left panel */
.veg{height:505px;padding:14px 12px;display:grid;grid-template-columns:1fr 1fr;column-gap:16px}
.veg .col{display:flex;flex-direction:column;justify-content:space-between}
.veg .col .ribbon{align-self:flex-start;margin-bottom:4px}
.sides{flex:1;padding:14px 12px;display:grid;grid-template-columns:1fr 1fr;column-gap:16px;position:relative}
.sides .col{display:flex;flex-direction:column;gap:6px}
.sides .ribbon{align-self:center;margin-bottom:4px}
.photo{border-radius:6px}
.photo-spice{width:110px;height:40px;background:radial-gradient(ellipse,#d8402a,#f3e3dc 70%)}
.photo-noodles{position:absolute;right:18px;bottom:10px;width:150px;height:90px;border-radius:50%;background:radial-gradient(ellipse,#d39b5c,#eee 72%)}
.footer{height:72px;display:flex;flex-direction:column;align-items:center;justify-content:center;gap:6px;color:#fff}
.footer .note{font:400 17px "Oswald",sans-serif;text-transform:uppercase}
/* middle panel */
.beverages{height:340px;padding:14px 14px 0;position:relative}
.beverages .head{text-align:center;margin-bottom:10px}
.bev-grid{display:grid;grid-template-columns:1fr 1fr;column-gap:22px}
.bev-grid .col{display:flex;flex-direction:column;gap:5px}
.photo-glass{position:absolute;right:22px;bottom:10px;width:160px;height:130px;background:radial-gradient(ellipse at 40% 40%,#cfe6a4,#e9f4f2 60%,#fff 80%)}
.desserts{height:130px;padding:10px 14px;display:grid;grid-template-columns:1fr 1fr;column-gap:22px}
.desserts .col{display:flex;flex-direction:column;gap:6px}
.desserts .ribbon{align-self:flex-start}
.info{display:grid;grid-template-columns:1fr 1fr;column-gap:12px;padding:12px 14px 0;height:150px}
.info .ribbon{margin-bottom:8px}
.contact-line{display:flex;align-items:flex-start;gap:6px;font-size:8.5px;margin-bottom:8px}
.contact-line svg{flex:none;width:11px;height:11px}
.hours{text-align:right;font-size:8.5px;line-height:1.3}
.hours p{margin:0 0 9px}
.hours .right-ribbon{text-align:right}
.cards{padding:6px 14px 0;height:110px}
.card-row{display:flex;gap:5px;margin:10px 0 8px}
.card-row span{width:42px;height:26px;border:1px solid #bbb;border-radius:2px;background:#eef0f3}
.fresh{font-size:12px}
.halal{padding:6px 14px 0;flex:1}
.halal p{margin:10px 0 2px;font-size:10px;color:var(--muted)}
.halal strong{font:600 13px "Open Sans",sans-serif;letter-spacing:.5px}
.photo-fruit{position:absolute;right:20px;top:700px;width:135px;height:220px;background:linear-gradient(160deg,#c7df7d,#f0b64c 50%,#e9d2c2)}
.beer{font:500 30px "Oswald",sans-serif;text-transform:uppercase;flex-direction:row}
/* right panel */
.title{height:330px;padding:26px 14px 0;text-align:center}
.flourish{width:90px;height:18px;margin:0 auto 12px;background:linear-gradient(90deg,transparent,var(--gold-dark),transparent);border-radius:50%}
.title h1{margin:0;font:400 27px "Rye",serif;letter-spacing:-.5px;line-height:1}
.title .eat{font:400 28px "Courgette",cursive;margin:14px 0 10px}
.title .service{display:inline-block;border-top:1px dotted var(--gold-dark);border-bottom:1px dotted var(--gold-dark);padding:4px 10px;font:300 26px "Oswald",sans-serif;text-transform:uppercase}
.brand-band{height:140px;position:relative;display:flex;align-items:center;justify-content:center}
.brand-band::before{content:"";position:absolute;left:0;right:0;top:24px;height:92px;background:var(--chalk)}
.brand-disc{position:relative;width:180px;height:180px;border-radius:50%;background:var(--paper);display:flex;flex-direction:column;align-items:center;justify-content:center;gap:10px}
.brand-mark{width:52px;height:52px;border-radius:50%;border:2px solid var(--ink)}
.brand-name{font:600 20px "Open Sans",sans-serif}
.photo-food{flex:1;background:linear-gradient(160deg,#e9dfd4,#b99a78 45%,#5d7a4a 70%,#d9c8b4)}
.phone-big{display:flex;align-items:center;justify-content:center;gap:14px;font:500 36px "Oswald",sans-serif}
.phone-big svg{width:32px;height:32px}
</style>
</head>
<body>
<main class="menu">

  <!-- Panel 1 -->
  <section class="panel">
    <div class="veg chalk">
      <div class="col">
        <span class="ribbon">Handi Se - Vegetarian</span>
        <div class="item"><span class="name">Paneer Makhani</span><span class="price">$8.99</span><span class="desc">Fresh home cheese folded into creamy tomato sauce</span></div>
        <div class="item"><span class="name">Panner Tikka Masala</span><span class="price">$8.99</span><span class="desc">Cottage cheese sauteed with bell pepper, onion folded into a spiced tomato sauce</span></div>
        <div class="item"><span class="name">Kadai Paneer</span><span class="price">$8.99</span><span class="desc">Fresh home made cubes of cheese stir fry in a kadai with onion, ginger, tomato &amp; bell pepper</span></div>
        <div class="item"><span class="name">Palak Paneer</span><span class="price">$8.49</span><span class="desc">Fresh spinach cooked with cubes of cheese &amp; seasoned with garlic</span></div>
        <div class="item"><span class="name">Mutter Paneer</span><span class="price">$8.99</span><span class="desc">Home made cheese cooked with green peas in a mildly spiced sauce</span></div>
        <div class="item"><span class="name">Shahi Paneer</span><span class="price">$10.99</span><span class="desc">Paneer cubes cooked in a rich creamy almond sauce</span></div>
        <div class="item"><span class="name">Paneer Bhurji</span><span class="price">$8.99</span><span class="desc">Fresh home made cheese grated &amp; cooked with green pepper, tomato &amp; onions</span></div>
        <div class="item"><span class="name">Malai Kofta</span><span class="price">$8.99</span><span class="desc">Cheese vegetable balls in a savory almond flavored creamy sauce</span></div>
        <div class="item"><span class="name">Navratan Korma</span><span class="price">$9.29</span><span class="desc">Combination of Italian veg &amp; fruit, cooked in a cashew &amp; almond sauce</span></div>
        <div class="item"><span class="name">Kaju Mushroom Mutter</span><span class="price">$9.29</span><span class="desc">Fresh mushroom, cashew, peas cooked in onion &amp; cashew sauce</span></div>
        <div class="item"><span class="name">Methi Malai Mutter</span><span class="price">$8.50</span><span class="desc">Fenugreek leaves cooked with peas in a cashew flavor lightly cream sauce</span></div>
      </div>
      <div class="col">
        <div class="item"><span class="name">Aloo Gobhi</span><span class="price">$8.50</span><span class="desc">A dry Indian dish made with potatoes, cauliflower &amp; ginger</span></div>
        <div class="item"><span class="name">Achari Baigan</span><span class="price">$8.49</span><span class="desc">Baby eggplant cooked in a spicy picklish flavor masala</span></div>
        <div class="item"><span class="name">Baigan Bharta</span><span class="price">$8.49</span><span class="desc">Eggplant roasted on charcoal, mixed &amp; cooked with onions &amp; tomatoes</span></div>
        <div class="item"><span class="name">Vegetable Jalfrezi</span><span class="price">$8.49</span><span class="desc">Mixed vegetable with cottage cheese mildly spiced</span></div>
        <div class="item"><span class="name">Zeera Aloo</span><span class="price">$7.50</span><span class="desc">Crispy potato stir fry with cumin seeds</span></div>
        <div class="item"><span class="name">Sarson Ka Saag</span><span class="price">$8.49</span><span class="desc">Mustard leaves cooked in a Punjabi style tastes really nice with makki ki roti</span></div>
        <div class="item"><span class="name">Chana Peshawari</span><span class="price">$8.49</span><span class="desc">Delicious chickpeas cooked in an exotic blend of North Indian spices</span></div>
        <div class="item"><span class="name">Chana Palak</span><span class="price">$8.49</span><span class="desc">Frontier chick peas cooked with fresh spinach</span></div>
        <div class="item"><span class="name">Punjabi Kadi</span><span class="price">$8.49</span><span class="desc">A stew made with yogurt &amp; chickpeas flour seasoned with spices</span></div>
        <div class="item"><span class="name">Daal Tarka Yellow</span><span class="price">$8.49</span><span class="desc">Slow simmered yellow lentils sauteed with tomato, ginger &amp; garlic</span></div>
        <div class="item"><span class="name">Daal Tarka Black</span><span class="price">$8.49</span><span class="desc">Slow simmered black lentils sauteed with tomato, ginger &amp; garlic</span></div>
        <div class="item"><span class="name">Daal Makhni</span><span class="price">$8.49</span><span class="desc">Classic lentils with kidney beans simmered in tomato &amp; light butter</span></div>
      </div>
    </div>

    <div class="sides">
      <div class="col">
        <span class="ribbon">Tandoori Bread</span>
        <div class="item"><span class="name">Tandoori Roti</span><span class="price">$1.75</span><span class="desc">Flat whole wheat bread baked in a clay oven</span></div>
        <div class="item"><span class="name">Tandoori Naan</span><span class="price">$1.75</span><span class="desc">Soft white bread baked in a clay oven</span></div>
        <div class="item"><span class="name">Garlic Naan</span><span class="price">$2.50</span><span class="desc">Naan flavoured with fresh garlic &amp; coriander</span></div>
        <div class="item"><span class="name">Lachha Paratha</span><span class="price">$2.50</span><span class="desc">Rich multilayered whole wheat bread baked in a clay oven</span></div>
        <div class="item"><span class="name">Onion Kulcha</span><span class="price">$2.99</span><span class="desc">Naan bread stuffed with seasoned finely chopped onions</span></div>
        <div class="item"><span class="name">Jalebi Paratha</span><span class="price">$2.99</span><span class="desc">Rich multilayered naan bread</span></div>
        <div class="item"><span class="name">Pudina Paratha</span><span class="price">$2.99</span><span class="desc">Tandoori paratha flavored with fresh mint</span></div>
        <div class="item"><span class="name">Keema Naan</span><span class="price">$3.99</span><span class="desc">Whole wheat bread stuffed with fresh chicken keema</span></div>
        <div class="item"><span class="name">Aloo Paratha</span><span class="price">$2.99</span><span class="desc">Whole wheat paratha stuffed with mildly spiced mashed potato</span></div>
        <div class="item"><span class="name">Gobhi Paratha</span><span class="price">$3.50</span><span class="desc">Wheat bread stuffed with mildly spiced cauliflower</span></div>
        <div class="photo photo-spice" role="img" aria-label="Photo of red chilli powder spilling from a jar"></div>
      </div>
      <div class="col">
        <span class="ribbon">Biryani &amp; Rice</span>
        <div class="item"><span class="name">Chicken Biryani</span><span class="price">$7.99</span><span class="desc">Boneless chicken cooked on low heat with long grain basmati rice</span></div>
        <div class="item"><span class="name">Goat Biryani</span><span class="price">$9.99</span><span class="desc">Goat cooked on low heat with long grain basmati rice</span></div>
        <div class="item"><span class="name">Lamb Biryani</span><span class="price">$9.99</span><span class="desc">Lamb cooked on low heat with long grain basmati rice</span></div>
        <div class="item"><span class="name">Shrimp Biryani</span><span class="price">$10.99</span><span class="desc">Shrimp cooked on low heat with long grain basmati rice</span></div>
        <div class="item"><span class="name">Vegetable Biryani</span><span class="price">$7.99</span><span class="desc">Basmati rice cooked with mixed vegetable in a blend of herbs nuts &amp; saffron</span></div>
        <div class="item"><span class="name">Zeera Rice</span><span class="price">$3.99</span></div>
        <div class="item"><span class="name">Peas Pulao</span><span class="price">$5.99</span></div>
        <div class="item"><span class="name">House Special Biryani</span><span class="price">$11.99</span><span class="desc">Long grain basmati rice flavored with saffron then sauteed together with shrimp, lamb &amp; chicken in a delicate blend of spices &amp; nuts</span></div>
      </div>
      <div class="photo photo-noodles" role="img" aria-label="Photo of a plate of stir-fried noodles with shrimp"></div>
    </div>

    <div class="footer chalk">
      <span class="ribbon">Tax is not included in these prices</span>
      <span class="note">Prices subject to change without notice</span>
    </div>
  </section>

  <!-- Panel 2 -->
  <section class="panel">
    <div class="beverages">
      <div class="head"><span class="ribbon">Beverages</span></div>
      <div class="bev-grid">
        <div class="col">
          <div class="item"><span class="name">Mango Lassi</span><span class="price">$3.50</span><span class="desc">A refreshing yogurt mango drink</span></div>
          <div class="item"><span class="name">Lassi (sweet or salted)</span><span class="price">$3.50</span><span class="desc">A delicious yogurt drink</span></div>
          <div class="item"><span class="name">Fresh Lemonade</span><span class="price">$2.99</span><span class="desc">A sweet &amp; sour lemon flavor drink</span></div>
          <div class="item"><span class="name">Pina Colada Virgin</span><span class="price">$3.99</span><span class="desc">Combination of pineapple juice and coconut cream</span></div>
          <div class="item"><span class="name">Strawberry Daiquiri Virgin</span><span class="price">$3.99</span><span class="desc">An ambrosial blend of strawberries &amp; citrus soda</span></div>
          <div class="item"><span class="name">Orange Juice</span><span class="price">$2.99</span></div>
          <div class="item"><span class="name">Pineapple Juice</span><span class="price">$2.99</span></div>
          <div class="item"><span class="name">Mango Juice</span><span class="price">$2.99</span></div>
          <div class="item"><span class="name">Masala Tea</span><span class="price">$1.99</span><span class="desc">Indian tea with a mixture of aromatic spices &amp; herbs</span></div>
          <div class="item"><span class="name">Coffee</span><span class="price">$1.99</span></div>
          <div class="item"><span class="name">Assorted Sodas, Ginger Ale</span><span class="price">$1.50</span></div>
        </div>
        <div class="col">
          <div class="item"><span class="name">Cold Beers</span><span class="price">$1.99</span><span class="desc">Domestic &amp; imported lagers, ales &amp; more</span></div>
          <div class="item"><span class="name">Indian Beers</span><span class="price"></span><span class="desc">Classic Indian lagers</span></div>
          <div class="item"><span class="name">Wines (750ml / 1.5 Lt)</span><span class="price">$22.00 / $38.00</span><span class="desc">Merlot - Cabernet - Chardonnay - Pinot Grigio</span></div>
        </div>
      </div>
      <div class="photo photo-glass" role="img" aria-label="Photo of a glass of iced lemonade with lime and mint"></div>
    </div>

    <div class="desserts chalk">
      <div class="col">
        <span class="ribbon">Desserts</span>
        <div class="item"><span class="name">Kheer</span><span class="price">$3.99</span><span class="desc">Basmati rice pudding flavoured with cardamom, nuts, raisins and topped with pistachio</span></div>
        <div class="item"><span class="name">Rasmalai (3 pc.)</span><span class="price">$3.99</span><span class="desc">Cold cheese dumpling flavoured with cardamom, saffron &amp; topped with lightly sweet milk syrup</span></div>
      </div>
      <div class="col">
        <div class="item"><span class="name">Gajar Halwa</span><span class="price">$3.99</span><span class="desc">Fresh carrot cooked with milk cottage, cheese &amp; nuts</span></div>
        <div class="item"><span class="name">Gulab Jamun (3 pc.)</span><span class="price">$3.99</span><span class="desc">Golden fries ball of milk pastry soaked in honey syrup topped with shredded coconut</span></div>
        <div class="item"><span class="name">Ice Cream</span><span class="price">$3.50</span><span class="desc">Mango or vanilla or chocolate flavour</span></div>
      </div>
    </div>

    <div class="info">
      <div class="contact">
        <span class="ribbon">Contact Us</span>
        <div class="contact-line"><svg viewBox="0 0 12 12"><circle cx="6" cy="6" r="6"/><path d="M6 2.5a2.2 2.2 0 0 0-2.2 2.2C3.8 6.5 6 9.5 6 9.5s2.2-3 2.2-4.8A2.2 2.2 0 0 0 6 2.5z" fill="#fff"/></svg><span>204-15 Linden Ave., Maple Heights,<br>NY 11000</span></div>
        <div class="contact-line"><svg viewBox="0 0 12 12"><circle cx="6" cy="6" r="6"/><path d="M4 3l1.2 1.3-.6.9c.4.9 1 1.5 1.9 1.9l.9-.6L8.7 7.7 8 8.8C5.5 8.6 3.4 6.5 3.2 4z" fill="#fff"/></svg><span>555-210-4400 / 4401</span></div>
        <div class="contact-line"><svg viewBox="0 0 12 12"><rect width="12" height="12" rx="2"/><rect x="3" y="5" width="6" height="4" fill="#fff"/><rect x="4" y="3" width="4" height="2" fill="#fff"/></svg><span>555-210-4420</span></div>
        <div class="contact-line"><svg viewBox="0 0 12 12"><circle cx="6" cy="6" r="6"/><rect x="3" y="4" width="6" height="4" fill="#fff"/></svg><span>saffroncourtnyc@mail.com</span></div>
      </div>
      <div class="hours">
        <div class="right-ribbon"><span class="ribbon">Business Hours</span></div>
        <p>Sunday To Thursday - 11:30am. To 12:00am.</p>
        <p>Friday To Saturday - 11:30am. To 01:00am.</p>
        <p>Lunch Special</p>
        <p>Monday To Sunday - 11:30am. To 04:00pm.</p>
      </div>
    </div>

    <div class="cards">
      <span class="ribbon">We accept all major credit cards</span>
      <div class="card-row"><span></span><span></span><span></span><span></span></div>
      <div class="fresh">Everything made Fresh to Order</div>
    </div>

    <div class="halal">
      <span class="ribbon">We serve halal food</span>
      <p>Spices as per customer's Choice</p>
      <strong>MILD - MEDIUM - SPICY</strong>
    </div>
    <div class="photo photo-fruit" role="img" aria-label="Photo of a hand holding a glass of fresh fruit salad with lime"></div>

    <div class="footer chalk beer">We deliver cold beer &amp; wine</div>
  </section>

  <!-- Panel 3 -->
  <section class="panel">
    <div class="title">
      <div class="flourish" role="img" aria-label="Gold decorative flourish"></div>
      <h1>THE BEST INDIAN CUISINE</h1>
      <div class="eat">Eat In . Take Out</div>
      <div class="service">Delivery &amp; Catering</div>
    </div>
    <div class="brand-band">
      <div class="brand-disc">
        <span class="brand-mark"></span>
        <span class="brand-name">Saffron Court</span>
      </div>
    </div>
    <div class="photo-food" role="img" aria-label="Photo of a chef tossing a fresh salad beside bowls of Indian dishes and spices"></div>
    <div class="footer chalk phone-big">
      <svg viewBox="0 0 32 32" fill="#fff"><path d="M4 12c0-4 5-6 12-6s12 2 12 6v2h-6v-3c-2-1-4-1-6-1s-4 0-6 1v3H4z"/><path d="M9 15h14l3 11H6z"/><circle cx="16" cy="20" r="3" fill="#1c1c1c"/></svg>
      <span>555-210-4400 / 4401</span>
    </div>
  </section>

</main>
</body>
</html>
```